Package design for supplement

We are looking to design a product packaing in Paperboard Jar. Our company sells varity of supplements. we had previously design in Stand up pouches but we needs new design in Jars. See attached all product information and logos

```html
<!DOCTYPE html>
<html lang="en">
<head>
<meta charset="utf-8">
<title>Verdane Naturals – Organic Psyllium Whole Husk Label</title>
<link rel="stylesheet" href="https://fonts.googleapis.com/css2?family=Cinzel:wght@500;600&family=Source+Sans+3:wght@400;600&display=swap">
<style>
  :root {
    --backdrop: #a0a0a0;
    --label-cream: #f6f5ec;
    --leaf-green: #3bb54a;
    --deep-green: #1f9a3c;
    --title-green: #1c8b3c;
    --slate: #3e5461;
    --gold: #d8a737;
    --gold-light: #f3d47a;
    --silver: #c9cbcd;
    --herb-tint: #cfe5c9;
  }
  * { margin: 0; padding: 0; box-sizing: border-box; }
  html, body {
    width: 1200px;
    height: 1081px;
    overflow: hidden;
    background: var(--backdrop);
  }
  .label {
    position: absolute;
    left: 420px;
    top: 255px;
    width: 360px;
    height: 590px;
    background: var(--label-cream);
    overflow: hidden;
  }
  .label-art {
    position: absolute;
    inset: 0;
  }
  .brand {
    position: absolute;
    top: 205px;
    left: 0;
    width: 100%;
    text-align: center;
    font-family: "Cinzel", serif;
    font-weight: 600;
    font-size: 27px;
    letter-spacing: 1px;
    color: var(--slate);
  }
  .product-title {
    position: absolute;
    top: 300px;
    left: 0;
    width: 100%;
    text-align: center;
    font-family: "Cinzel", serif;
    font-weight: 500;
    font-size: 29px;
    line-height: 32px;
    color: var(--title-green);
  }
  .divider {
    position: absolute;
    top: 412px;
    left: 118px;
    width: 124px;
    height: 2px;
    background: var(--slate);
    border-radius: 2px;
  }
  .herb {
    position: absolute;
    background: linear-gradient(180deg, rgba(207,229,201,0.2), var(--herb-tint));
    border-radius: 40% 40% 8px 8px;
  }
  .herb-right { left: 285px; top: 370px; width: 60px; height: 100px; }
  .herb-left { left: 8px; top: 420px; width: 66px; height: 92px; }
  .badges {
    position: absolute;
    left: 6px;
    top: 518px;
    display: flex;
    gap: 4px;
  }
  .badge {
    width: 28px;
    height: 28px;
    border-radius: 50%;
    background: var(--deep-green);
    border: 2px solid #fff;
  }
  .badge-light { background: #fff; border-color: var(--slate); }
  .net-weight {
    position: absolute;
    right: 12px;
    top: 505px;
    text-align: right;
    font-family: "Source Sans 3", sans-serif;
    color: #fff;
    font-size: 11px;
    line-height: 15px;
  }
  .net-weight strong { font-weight: 600; font-size: 11.5px; }
</style>
</head>
<body>
  <div class="label">
    <svg class="label-art" width="360" height="590" viewBox="0 0 360 590" aria-hidden="true">
      <defs>
        <linearGradient id="goldBand" x1="0" y1="0" x2="0" y2="1">
          <stop offset="0" stop-color="var(--gold)"/>
          <stop offset="0.5" stop-color="var(--gold-light)"/>
          <stop offset="1" stop-color="var(--gold)"/>
        </linearGradient>
        <linearGradient id="silverRim" x1="0" y1="0" x2="1" y2="0">
          <stop offset="0" stop-color="#9ea1a4"/>
          <stop offset="0.5" stop-color="#eef0f1"/>
          <stop offset="1" stop-color="#9ea1a4"/>
        </linearGradient>
      </defs>
      <!-- lid rim -->
      <rect x="0" y="0" width="360" height="10" fill="url(#silverRim)"/>
      <!-- top wave -->
      <path d="M0 10 H360 V40 C300 10 230 30 170 70 C120 100 60 110 0 112 Z" fill="var(--leaf-green)"/>
      <path d="M0 98 C70 95 120 80 170 55 C230 25 300 15 360 40 V62 C300 30 240 40 180 75 C120 105 60 118 0 120 Z" fill="#fff"/>
      <path d="M0 122 C60 120 110 110 160 90 C110 120 60 132 0 136 Z" fill="var(--deep-green)"/>
      <path d="M250 40 C290 25 330 28 360 42 V50 C330 38 290 36 250 40 Z" fill="var(--deep-green)"/>
      <!-- upper gold band -->
      <rect x="0" y="144" width="360" height="8" fill="url(#goldBand)"/>
      <!-- bottom wave -->
      <path d="M0 510 C70 505 120 490 180 465 C240 440 300 435 360 445 V568 H0 Z" fill="var(--leaf-green)"/>
      <path d="M0 500 C70 495 130 478 180 458 C240 433 300 428 360 438 V448 C300 438 240 444 182 468 C125 492 70 507 0 512 Z" fill="#fff"/>
      <path d="M80 538 C120 532 160 522 200 505 C170 525 130 540 80 545 Z" fill="#fff"/>
      <!-- lower gold band and rim -->
      <rect x="0" y="566" width="360" height="8" fill="url(#goldBand)"/>
      <rect x="0" y="574" width="360" height="16" fill="url(#silverRim)"/>
    </svg>

    <div class="herb herb-right" role="img" aria-label="Fine line botanical sketch of a flowering psyllium plant"></div>
    <div class="herb herb-left" role="img" aria-label="Fine line botanical sketch of a flowering psyllium plant"></div>

    <div class="brand">Verdane Naturals</div>

    <h1 class="product-title">Organic<br>Psyllium<br>Whole Husk</h1>
    <div class="divider"></div>

    <div class="badges">
      <span class="badge"></span>
      <span class="badge badge-light"></span>
    </div>

    <p class="net-weight">Net Weight<br><strong>16oz (453.6g)</strong></p>
  </div>
</body>
</html>
```